Homepage Redesign - Hi-tech business Law Firm

I'm looking for an updated graphic design (pdf file) for the homepage of dorvantlegal.ca (and which will form the general template of the other pages - but you don't need to design that). Detailed specs are in the Word file.

Deliverable is 1 pdf file that I find good looking, that sets forth the layout of the new page.

Target Market(s)

Sophisticated customers

Industry/Entity Type

Legal

Number of Pages Required

1 page

Requirements
Nice to have
• For a main background, tech type images to do with high powered boardrooms, computers, graphs, numbers, high tech manufacturing lines etc. Also, I tend to like blues and light greys, and uploaded a file today that shows my generally preferred layout, which a few of you have been getting close to.
Should not have
• Any mention of 'Personal Injury,' backgrounds that include books, or buildings with roman columns. Page should not be in dark colors or harsh on the eyes.

```html
<!DOCTYPE html>
<html lang="en">
<head>
<meta charset="utf-8">
<title>Dorvant Legal — Business Law Firm</title>
<link href="https://fonts.googleapis.com/css2?family=Playfair+Display:wght@400;600;700&family=Poppins:wght@300;400;500;600&display=swap" rel="stylesheet">
<style>
:root{
  --navy:#0e3a63;
  --blue:#14507f;
  --ink:#1c2430;
  --text:#555d68;
  --muted:#8a929c;
  --line:#d9dee5;
  --pale:#eef1f5;
  --white:#ffffff;
  --black:#121212;
}
*{box-sizing:border-box;margin:0;padding:0}
html,body{width:1200px;height:3228px;overflow:hidden}
body{position:relative;background:var(--white);font-family:"Poppins",sans-serif;color:var(--text);font-size:13px;line-height:1.6}

/* header */
.site-header{position:absolute;left:0;top:0;width:1200px;height:112px;background:var(--white);display:flex;align-items:center;padding:0 64px;z-index:5}
.brand{display:flex;align-items:center;gap:12px}
.brand-box{width:44px;height:44px;background:var(--navy)}
.brand-name{font-family:"Playfair Display",serif;font-weight:700;font-size:22px;color:var(--navy);letter-spacing:1px;text-transform:uppercase;line-height:1.1}
.brand-tag{font-size:10px;color:var(--muted);font-style:italic}
.header-right{margin-left:auto;text-align:right}
.header-phone{font-weight:600;color:var(--navy);font-size:15px;display:flex;align-items:center;justify-content:flex-end;gap:8px}
.nav{display:flex;gap:34px;margin-top:10px;font-size:13px;color:var(--ink)}
.nav a{color:inherit;text-decoration:none}

/* hero */
.hero{position:absolute;left:0;top:112px;width:1200px;height:490px;background:linear-gradient(100deg,#2a2723 0%,#4a4035 45%,#6b5f52 70%,#8d8275 100%)}
.hero-person{position:absolute;left:600px;top:190px;width:280px;height:412px;background:linear-gradient(180deg,#7a6e62 0%,#1f2f45 40%,#17263a 100%);border-radius:130px 130px 0 0;z-index:2}
.hero-title{position:absolute;left:64px;top:262px;font-family:"Playfair Display",serif;font-size:44px;line-height:1.12;color:var(--white);font-weight:600;z-index:3}
.hero-actions{position:absolute;left:64px;top:462px;display:flex;gap:36px;z-index:3}
.btn{display:inline-block;padding:10px 34px;border-radius:24px;font-size:13px;font-weight:500;letter-spacing:.5px;text-transform:uppercase;line-height:1.4}
.btn-solid{background:var(--blue);color:var(--white)}
.btn-ghost{border:1.5px solid var(--white);color:var(--white)}
.btn-sm{padding:7px 22px;font-size:11px;background:var(--blue);color:var(--white);border-radius:18px}

/* case evaluation */
.case-card{position:absolute;left:72px;top:540px;width:416px;height:560px;background:var(--white);border-radius:14px;box-shadow:0 6px 30px rgba(20,40,70,.18);padding:32px 30px;z-index:4}
.case-card h2{font-family:"Playfair Display",serif;color:var(--navy);font-size:24px;text-align:center;font-weight:600}
.case-card .sub{text-align:center;font-size:12px;margin:6px 0 24px}
.field-row{display:flex;gap:14px;margin-bottom:16px}
.field{flex:1;height:36px;border:1px solid var(--line);border-radius:4px;padding:8px 12px;font-size:11px;color:var(--muted)}
.field-area{height:150px;margin-bottom:20px}
.consent{font-size:11px;line-height:1.5;margin-bottom:22px}
.case-card .btn{display:block;width:170px;margin:0 auto;text-align:center;text-transform:none;padding:9px 0}

/* intro */
.intro{position:absolute;left:528px;top:740px;width:600px}
.badge-row{display:flex;align-items:center;gap:18px;margin-bottom:60px}
.badge{width:200px;height:42px;background:#c9302c;border-radius:3px;flex:none}
.badge-note{font-size:11px;line-height:1.5;color:var(--muted);width:360px}
.intro h2{font-family:"Playfair Display",serif;font-size:25px;line-height:1.25;color:var(--ink);font-weight:700;margin-bottom:16px}
.intro p{font-size:12px;margin-bottom:14px}
.intro .btn{margin-left:90px}

/* practice areas */
.practice{position:absolute;left:0;top:1222px;width:1200px;height:540px;background:var(--pale)}
.section-title{font-family:"Playfair Display",serif;font-size:22px;color:var(--navy);text-align:center;letter-spacing:1px;font-weight:600}
.practice .section-title{margin-top:38px}
.cards{position:absolute;left:72px;top:110px;display:flex;gap:24px}
.card{width:246px;height:410px;background:var(--white);border-radius:10px;box-shadow:0 4px 18px rgba(20,40,70,.1);padding:78px 20px 20px;position:relative}
.card-icon{position:absolute;left:-10px;top:-26px;width:84px;height:84px;border-radius:12px;background:var(--navy);display:flex;align-items:center;justify-content:center}
.card h3{font-family:"Playfair Display",serif;font-size:13.5px;color:var(--ink);text-transform:uppercase;text-align:center;font-weight:700;margin-bottom:6px;white-space:nowrap}
.card .desc{font-size:10.5px;text-align:center;line-height:1.45;margin-bottom:14px;height:46px}
.card ul{list-style:none;margin-bottom:20px}
.card li{display:flex;align-items:center;gap:8px;font-size:11px;margin-bottom:7px;color:var(--ink)}
.card .btn-sm{display:block;width:110px;text-align:center;padding:6px 0}

/* testimonials */
.testimonials{position:absolute;left:0;top:1846px;width:1200px;height:336px;background:var(--blue)}
.testimonials .section-title{color:var(--white);margin-top:40px}
.quotes{position:absolute;left:72px;top:104px;display:flex;gap:40px}
.quote{width:325px;height:176px;background:var(--white);border-radius:8px;padding:20px 24px}
.stars{display:flex;gap:6px;margin-bottom:10px}
.quote p{font-size:11px;line-height:1.5;margin-bottom:12px}
.reviewer{display:flex;align-items:center;gap:10px}
.avatar{width:34px;height:34px;border-radius:50%;background:linear-gradient(135deg,#b9c3ce,#7f8b98)}
.reviewer b{display:block;font-size:11px;color:var(--ink);font-weight:600}
.reviewer span{font-size:10px;color:var(--muted)}

/* news */
.news{position:absolute;left:0;top:2240px;width:1200px;height:700px}
.news .section-title{margin-top:40px}
.news-feature{position:absolute;left:72px;top:120px;width:340px}
.news-feature .img{width:340px;height:240px;border-radius:6px;background:linear-gradient(135deg,#c9bfb3,#6c7684)}
.news-feature h3{font-size:28px;font-weight:500;color:var(--ink);line-height:1.2;margin:22px 0 10px}
.news-feature p{font-size:12px;margin-bottom:12px}
.more{font-size:13px;color:var(--blue);font-weight:600;display:flex;align-items:center;gap:8px}
.news-list{position:absolute;left:440px;top:120px;width:690px}
.news-item{display:flex;gap:24px;margin-bottom:34px}
.news-item .img{width:200px;height:130px;border-radius:6px;background:linear-gradient(135deg,#d3cbc1,#6f7a88);flex:none}
.news-item h4{font-family:"Playfair Display",serif;font-size:15px;color:var(--blue);font-weight:600;margin-bottom:4px}
.news-item p{font-size:11px;line-height:1.5;margin-bottom:8px}

/* share */
.share{position:absolute;left:0;top:2950px;width:1200px;height:68px;background:var(--blue);display:flex;align-items:center;justify-content:center;gap:34px}
.share b{color:var(--white);font-size:14px;font-weight:600;letter-spacing:1px}
.share-dots{display:flex;gap:22px}
.share-dot{width:22px;height:22px;border-radius:50%;background:var(--white)}

/* footer */
.site-footer{position:absolute;left:0;top:3018px;width:1200px;height:210px;background:var(--black);color:#c9ccd1;padding:34px 64px;display:flex}
.foot-brand{width:340px}
.foot-brand .brand-name{color:var(--white)}
.foot-brand .brand-box{background:var(--white)}
.foot-region{margin-top:14px;font-size:12px;letter-spacing:1px;color:var(--white)}
.foot-phone{font-size:12px;margin-top:8px;display:flex;gap:8px;align-items:center}
.foot-links{width:200px;font-size:12px;line-height:1.9}
.foot-links h5{font-size:11px;font-weight:600;color:var(--muted);letter-spacing:1px;margin-bottom:4px}
.foot-about{flex:1;font-size:11px;line-height:1.6}
.foot-about p{margin-bottom:6px}
</style>
</head>
<body>

<svg width="0" height="0" style="position:absolute"><defs><path id="st" d="M10 1l2.7 6 6.3.6-4.8 4.2 1.5 6.2L10 14.7 4.3 18l1.5-6.2L1 7.6l6.3-.6z"/><g id="tick"><circle cx="12" cy="12" r="11" fill="#14507f"/><path d="M7 12l3 3 7-7" stroke="#fff" stroke-width="2.5" fill="none"/></g><g id="arrow"><circle cx="12" cy="12" r="11" fill="#14507f"/><path d="M10 7l5 5-5 5" stroke="#fff" stroke-width="2" fill="none"/></g><path id="phone" d="M6.6 10.8a15 15 0 0 0 6.6 6.6l2.2-2.2a1 1 0 0 1 1-.25 11.4 11.4 0 0 0 3.6.57 1 1 0 0 1 1 1V20a1 1 0 0 1-1 1A17 17 0 0 1 3 4a1 1 0 0 1 1-1h3.5a1 1 0 0 1 1 1c0 1.25.2 2.45.57 3.57a1 1 0 0 1-.25 1z"/></defs></svg>

<header class="site-header">
  <div class="brand">
    <div class="brand-box"></div>
    <div>
      <div class="brand-name">Dorvant Legal</div>
      <div class="brand-tag">"Getting the results that matter"</div>
    </div>
  </div>
  <div class="header-right">
    <div class="header-phone"><svg width="14" height="14" viewBox="0 0 24 24"><use href="#phone" fill="#0e3a63"/></svg>(800) 555-0142</div>
    <nav class="nav"><a>Home</a><a>Practice Areas</a><a>About</a><a>News</a><a>Legal Resources</a><a>Contact</a></nav>
  </div>
</header>

<section class="hero" role="img" aria-label="Photo of a modern office interior with soft warm lighting"></section>
<div class="hero-person" role="img" aria-label="Photo of the lead lawyer in a dark suit, arms crossed"></div>
<h1 class="hero-title">Winning.<br>My clients depend on me for it.<br>Shouldn't you?</h1>
<div class="hero-actions"><span class="btn btn-solid">Read More</span><span class="btn btn-ghost">Video Library</span></div>

<form class="case-card">
  <h2>Case Evaluation</h2>
  <p class="sub">Fill out the form to schedule your initial<br>consult with our lawyers</p>
  <div class="field-row"><div class="field">First Name</div><div class="field">Last Name</div></div>
  <div class="field-row"><div class="field">Email</div><div class="field">Phone Number</div></div>
  <div class="field field-area">Case Details</div>
  <p class="consent">* By using this site and/or submitting this form, I agree to the Privacy Policy and Terms of Use.</p>
  <span class="btn btn-solid">Submit Details</span>
</form>

<section class="intro">
  <div class="badge-row">
    <div class="badge" role="img" aria-label="Lawyer rating badge"></div>
    <p class="badge-note">An excellent rating for a lawyer with many reviewers. This rating indicates the advocate is widely respected by their peers for high professional achievement and ethical standards.</p>
  </div>
  <h2>Your Experienced Toronto and Hamilton Lawyers – Getting the Results That Matter</h2>
  <p>Dorvant Legal is a boutique litigation firm with law offices in Toronto and Hamilton. We concentrate our legal practice on complex business litigation, professional negligence, construction claims and insurance coverage disputes. We take an innovative approach to our client's legal problems, and are guided by the philosophy that our job is to get results.</p>
  <p>The lawyers at Dorvant Legal have the reputation for vigorously representing their clients' interests and competing hard to obtain the best possible results. With experience at all stages of legal disputes, the lawyers at Dorvant Legal are equally at home negotiating in a boardroom or presenting a case at trial. We hope that you take the time to explore our website to find out more about our record of excellence, expertise and many years of experience.</p>
  <span class="btn btn-solid">Read More</span>
</section>

<section class="practice">
  <h2 class="section-title">PRACTICE AREAS</h2>
  <div class="cards">
    <article class="card">
      <div class="card-icon"><svg width="42" height="42" viewBox="0 0 24 24" fill="none" stroke="#fff" stroke-width="1.5"><rect x="3" y="7" width="18" height="13" rx="2"/><path d="M9 7V5h6v2M3 12h18"/></svg></div>
      <h3>Business Litigation</h3>
      <p class="desc">Practical, focused advice for companies facing disputes with partners, suppliers and clients.</p>
      <ul>
        <li><svg width="12" height="12" viewBox="0 0 24 24"><use href="#tick"/></svg>Breach of Contract</li>
        <li><svg width="12" height="12" viewBox="0 0 24 24"><use href="#tick"/></svg>Shareholder Disputes</li>
        <li><svg width="12" height="12" viewBox="0 0 24 24"><use href="#tick"/></svg>Partnership Claims</li>
        <li><svg width="12" height="12" viewBox="0 0 24 24"><use href="#tick"/></svg>Injunctions</li>
        <li><svg width="12" height="12" viewBox="0 0 24 24"><use href="#tick"/></svg>Commercial Leasing</li>
        <li><svg width="12" height="12" viewBox="0 0 24 24"><use href="#tick"/></svg>Debt Recovery</li>
      </ul>
      <span class="btn-sm">Read More</span>
    </article>
    <article class="card">
      <div class="card-icon"><svg width="42" height="42" viewBox="0 0 24 24" fill="none" stroke="#fff" stroke-width="1.5"><path d="M12 3v18M5 21h14M4 8h16M4 8l-2 6h4zM20 8l-2 6h4z"/></svg></div>
      <h3>Professional Negligence</h3>
      <p class="desc">Holding advisors to account when professional errors cause real financial loss.</p>
      <ul>
        <li><svg width="12" height="12" viewBox="0 0 24 24"><use href="#tick"/></svg>Accountant Liability</li>
        <li><svg width="12" height="12" viewBox="0 0 24 24"><use href="#tick"/></svg>Lawyer Negligence</li>
        <li><svg width="12" height="12" viewBox="0 0 24 24"><use href="#tick"/></svg>Engineer Claims</li>
        <li><svg width="12" height="12" viewBox="0 0 24 24"><use href="#tick"/></svg>Broker Errors</li>
        <li><svg width="12" height="12" viewBox="0 0 24 24"><use href="#tick"/></svg>Appraiser Claims</li>
        <li><svg width="12" height="12" viewBox="0 0 24 24"><use href="#tick"/></svg>Advisor Disputes</li>
      </ul>
      <span class="btn-sm">Read More</span>
    </article>
    <article class="card">
      <div class="card-icon"><svg width="42" height="42" viewBox="0 0 24 24" fill="none" stroke="#fff" stroke-width="1.5"><path d="M3 21h18M5 21V10l7-5 7 5v11M9 21v-6h6v6"/></svg></div>
      <h3>Construction</h3>
      <p class="desc">Resolving project disputes for owners, contractors and trades across Ontario.</p>
      <ul>
        <li><svg width="12" height="12" viewBox="0 0 24 24"><use href="#tick"/></svg>Lien Claims</li>
        <li><svg width="12" height="12" viewBox="0 0 24 24"><use href="#tick"/></svg>Payment Disputes</li>
        <li><svg width="12" height="12" viewBox="0 0 24 24"><use href="#tick"/></svg>Delay Claims</li>
        <li><svg width="12" height="12" viewBox="0 0 24 24"><use href="#tick"/></svg>Deficiency Claims</li>
        <li><svg width="12" height="12" viewBox="0 0 24 24"><use href="#tick"/></svg>Contract Review</li>
      </ul>
      <span class="btn-sm">Read More</span>
    </article>
    <article class="card">
      <div class="card-icon"><svg width="42" height="42" viewBox="0 0 24 24" fill="none" stroke="#fff" stroke-width="1.5"><path d="M12 3l8 3v6c0 5-3.5 8-8 9-4.5-1-8-4-8-9V6z"/><path d="M8.5 12l2.5 2.5 4.5-4.5"/></svg></div>
      <h3>Insurance</h3>
      <p class="desc">Resolving coverage disputes between policyholders and insurers with precision.</p>
      <ul>
        <li><svg width="12" height="12" viewBox="0 0 24 24"><use href="#tick"/></svg>Coverage Disputes</li>
        <li><svg width="12" height="12" viewBox="0 0 24 24"><use href="#tick"/></svg>Denied Claims</li>
        <li><svg width="12" height="12" viewBox="0 0 24 24"><use href="#tick"/></svg>Bad Faith Claims</li>
        <li><svg width="12" height="12" viewBox="0 0 24 24"><use href="#tick"/></svg>Business Interruption</li>
        <li><svg width="12" height="12" viewBox="0 0 24 24"><use href="#tick"/></svg>Property Loss</li>
      </ul>
      <span class="btn-sm">Read More</span>
    </article>
  </div>
</section>

<section class="testimonials">
  <h2 class="section-title">WHAT CUSTOMER SAYS</h2>
  <div class="quotes">
    <blockquote class="quote">
      <div class="stars"><svg width="96" height="16" viewBox="0 0 120 20"><g fill="#0e3a63"><use href="#st"/><use href="#st" x="24"/><use href="#st" x="48"/><use href="#st" x="72"/><use href="#st" x="96"/></g></svg></div>
      <p>Clear advice, fast answers and a result far better than we expected. The team understood our business from day one.</p>
      <div class="reviewer"><div class="avatar"></div><div><b>Dana Whitfield</b><span>Client</span></div></div>
    </blockquote>
    <blockquote class="quote">
      <div class="stars"><svg width="96" height="16" viewBox="0 0 120 20"><g fill="#0e3a63"><use href="#st"/><use href="#st" x="24"/><use href="#st" x="48"/><use href="#st" x="72"/><use href="#st" x="96"/></g></svg></div>
      <p>They handled a complex contract dispute with real skill and kept us informed at every stage of the process.</p>
      <div class="reviewer"><div class="avatar"></div><div><b>Dana Whitfield</b><span>Client</span></div></div>
    </blockquote>
    <blockquote class="quote">
      <div class="stars"><svg width="96" height="16" viewBox="0 0 120 20"><g fill="#0e3a63"><use href="#st"/><use href="#st" x="24"/><use href="#st" x="48"/><use href="#st" x="72"/><use href="#st" x="96"/></g></svg></div>
      <p>Professional, responsive and tough when it counted. I would recommend this firm to any business owner.</p>
      <div class="reviewer"><div class="avatar"></div><div><b>Dana Whitfield</b><span>Client</span></div></div>
    </blockquote>
  </div>
</section>

<section class="news">
  <h2 class="section-title">RECENT NEWS</h2>
  <article class="news-feature">
    <div class="img" role="img" aria-label="Photo of two professionals reviewing documents at a desk"></div>
    <h3>Lorem ipsum dolor sit amet</h3>
    <p>Lorem ipsum dolor sit amet, consectetur adipiscing elit, sed do eiusmod tempor incididunt ut labore et dolore.</p>
    <span class="more">READ MORE <svg width="16" height="16" viewBox="0 0 24 24"><use href="#arrow"/></svg></span>
  </article>
  <div class="news-list">
    <article class="news-item">
      <div class="img" role="img" aria-label="Photo of a business meeting around a table"></div>
      <div><h4>Lorem ipsum dolor sit amet</h4><p>Lorem ipsum dolor sit amet, consectetur adipiscing elit, sed do eiusmod tempor incididunt ut labore et dolore magna aliqua. Ut enim ad minim veniam, quis nostrud exercitation ullamco laboris nisi ut aliquip ex ea commodo consequat.</p><span class="more">Read more <svg width="14" height="14" viewBox="0 0 24 24"><use href="#arrow"/></svg></span></div>
    </article>
    <article class="news-item">
      <div class="img" role="img" aria-label="Photo of a lawyer consulting a client"></div>
      <div><h4>Lorem ipsum dolor sit amet</h4><p>Lorem ipsum dolor sit amet, consectetur adipiscing elit, sed do eiusmod tempor incididunt ut labore et dolore magna aliqua. Ut enim ad minim veniam, quis nostrud exercitation ullamco laboris nisi ut aliquip ex ea commodo consequat.</p><span class="more">Read more <svg width="14" height="14" viewBox="0 0 24 24"><use href="#arrow"/></svg></span></div>
    </article>
    <article class="news-item">
      <div class="img" role="img" aria-label="Photo of a handshake over signed documents"></div>
      <div><h4>Lorem ipsum dolor sit amet</h4><p>Lorem ipsum dolor sit amet, consectetur adipiscing elit, sed do eiusmod tempor incididunt ut labore et dolore magna aliqua. Ut enim ad minim veniam, quis nostrud exercitation ullamco laboris nisi ut aliquip ex ea commodo consequat.</p><span class="more">Read more <svg width="14" height="14" viewBox="0 0 24 24"><use href="#arrow"/></svg></span></div>
    </article>
  </div>
</section>

<section class="share">
  <b>SHARE THIS PAGE</b>
  <div class="share-dots">
    <span class="share-dot" aria-label="Share link"></span>
    <span class="share-dot" aria-label="Share link"></span>
    <span class="share-dot" aria-label="Share link"></span>
    <span class="share-dot" aria-label="Share link"></span>
  </div>
</section>

<footer class="site-footer">
  <div class="foot-brand">
    <div class="brand"><div class="brand-box"></div><div class="brand-name">Dorvant Legal</div></div>
    <div class="foot-region">GTA – HAMILTON – NIAGARA</div>
    <div class="foot-phone"><svg width="12" height="12" viewBox="0 0 24 24"><use href="#phone" fill="#c9ccd1"/></svg>(800) 555-0142</div>
  </div>
  <div class="foot-links">
    <h5>QUICK LINKS</h5>
    Home<br>About<br>Resources<br>Blog
  </div>
  <div class="foot-about">
    <p>DORVANT LEGAL IS A BOUTIQUE LAW OFFICE CONCENTRATING IN COMPLEX BUSINESS LITIGATION, PROFESSIONAL NEGLIGENCE, CONSTRUCTION AND INSURANCE COVERAGE DISPUTES. WE SERVE CLIENTS ACROSS THE GREATER TORONTO AREA. VISIT DORVANTLEGAL.CA</p>
    <p>Hamilton Office: 18 Keller Street East, Suite 210, Hamilton, ON L8N 0A1<br>Toronto Office: 240 Alder Street W, Suite 900, Toronto, ON M5H 0B2<br>Niagara Office: 7 Lindell Drive, Niagara Falls, ON L2E 0C3</p>
  </div>
</footer>

</body>
</html>
```